Single Page Digital Brochure

We are a Sydney based finance company. We lend money to developers. Please see attached example of what we are looking to have produced. We just need a design which can be posted on LINKEDIN

Target Market(s)

Property Developers who are borrowing money

Industry/Entity Type

Finance

Requirements
Must have
• Australian relevant imagery.

TEXT TO INCLUDE:

New Offering from Ferngate Lending
Nice to have
• Design and colour scheme based around our logo (attached)

Please include the same text as the attachment

Please make the design based loosely on the attachment. But do not copy the attachement
Should not have
• Remove Text: 'Settle in under four days'

```html
<!DOCTYPE html>
<html lang="en">
<head>
<meta charset="utf-8">
<title>New Offering from Ferngate Lending</title>
<link rel="stylesheet" href="https://fonts.googleapis.com/css2?family=Cinzel:wght@600;700&family=Roboto:wght@400;500;700&display=swap">
<style>
  :root {
    --page-bg: #231f20;
    --panel: #2d2e30;
    --panel-deep: #252628;
    --stripe: #1b1b1c;
    --sky-light: #e4e4e4;
    --sky-mid: #b9b9b9;
    --skyline: #7d7d7d;
    --bridge: #a8a8a8;
    --water: #3a3a3a;
    --water-deep: #151515;
    --text: #ffffff;
    --text-soft: #e6e6e6;
    --accent: #7dc242;
    --brand-dot: #2a5e3a;
  }
  * { box-sizing: border-box; margin: 0; padding: 0; }
  html, body { width: 1200px; height: 1200px; overflow: hidden; }
  body { background: var(--page-bg); font-family: "Roboto", Arial, sans-serif; }

  .brochure {
    position: absolute;
    left: 40px; top: 285px;
    width: 1120px; height: 631px;
  }
  .brochure__shapes { position: absolute; inset: 0; width: 100%; height: 100%; }

  .offer {
    position: absolute;
    left: 37px; top: 0;
    width: 680px; height: 100%;
    color: var(--text);
  }
  .offer__title {
    position: absolute; top: 34px;
    font-family: "Cinzel", "Times New Roman", serif;
    font-weight: 700;
    font-size: 44px;
    line-height: 38px;
    letter-spacing: 0.5px;
  }
  .offer__headline {
    position: absolute; top: 236px;
    font-weight: 700; font-size: 23px;
    color: var(--accent);
    letter-spacing: 0.2px;
  }
  .terms {
    position: absolute; top: 277px;
    list-style: none;
    font-size: 15px; line-height: 23.4px;
    color: var(--text-soft);
  }
  .terms__label { font-weight: 500; color: var(--text); margin-right: 6px; }
  .terms__value--strong { font-weight: 700; color: var(--text); }

  .brand {
    position: absolute; top: 550px;
    display: flex; align-items: center; gap: 12px;
  }
  .brand__dot { width: 22px; height: 22px; border-radius: 50%; background: var(--brand-dot); }
  .brand__name {
    font-family: "Cinzel", "Times New Roman", serif;
    font-weight: 600; font-size: 23px;
    color: var(--text);
    letter-spacing: 0.4px;
  }
  .contact {
    position: absolute; top: 598px;
    font-size: 13.5px; color: var(--text-soft);
  }
  .contact__detail { font-weight: 700; color: var(--accent); }
</style>
</head>
<body>
  <section class="brochure">
    <svg class="brochure__shapes" viewBox="0 0 1120 631" xmlns="http://www.w3.org/2000/svg">
      <defs>
        <linearGradient id="panelShade" x1="0" y1="0" x2="0" y2="1">
          <stop offset="0" stop-color="var(--panel)"/>
          <stop offset="1" stop-color="var(--panel-deep)"/>
        </linearGradient>
        <linearGradient id="cityTones" x1="0" y1="0" x2="0.15" y2="1">
          <stop offset="0" stop-color="var(--sky-mid)"/>
          <stop offset="0.18" stop-color="var(--sky-light)"/>
          <stop offset="0.38" stop-color="var(--sky-mid)"/>
          <stop offset="0.5" stop-color="var(--skyline)"/>
          <stop offset="0.6" stop-color="var(--bridge)"/>
          <stop offset="0.72" stop-color="var(--skyline)"/>
          <stop offset="0.82" stop-color="var(--water)"/>
          <stop offset="1" stop-color="var(--water-deep)"/>
        </linearGradient>
      </defs>
      <polygon class="panel" points="0,0 713,0 818,631 0,631" fill="url(#panelShade)"/>
      <polygon class="divider" points="713,0 731,0 836,631 818,631" fill="var(--stripe)"/>
      <polygon class="city-photo" points="731,0 1120,0 1120,631 836,631" fill="url(#cityTones)"
        role="img" aria-label="Black and white photograph of an Australian city skyline under cloudy sky with an arched stone bridge over a river at dusk"/>
    </svg>

    <div class="offer">
      <h1 class="offer__title">New Offering<br>from<br>Ferngate<br>Lending</h1>
      <h2 class="offer__headline">We Did. Just Last Week.</h2>
      <ul class="terms">
        <li><span class="terms__label">Loan Amout:</span>$75,000</li>
        <li><span class="terms__label">Rate:</span><span class="terms__value--strong">7.79%</span></li>
        <li><span class="terms__label">Term:</span>12 months</li>
        <li><span class="terms__label">Repayments:</span>Capitalised</li>
        <li><span class="terms__label">Security:</span>2x Sydney Residential Properties</li>
        <li><span class="terms__label">Purpose:</span>Business Working Capital</li>
      </ul>
      <div class="brand">
        <span class="brand__dot"></span>
        <span class="brand__name">Ferngate Lending</span>
      </div>
      <p class="contact">Call Mara today on <span class="contact__detail">0400 555 218</span> or <span class="contact__detail">mara@ferngatelending.com.au</span></p>
    </div>
  </section>
</body>
</html>
```